Quiet Hollow - New Product needs a Label

We need a package label for a new project that will come to market soon. The company is based in Canada and will need to show 'Made in Canada' with a Canadian flag.

The product is called Quiet Hollow. It is an odour eliminator. It will be in a dark brown plastic container that can be opened and left open in a room.

It can be used to help eliminate a number of different types of smoke; cigarette, pot or even fireplace smoke. We believe that 'no one should know what you smoke'.

We would like to see designs that reflect the intent of the product - to cover smoke. So far we've only thought that smokey colours like smokey green, smokey lavender and smokey grey or other grey tone colours would make sense. Update: I have removed the image that I 'doodled' on my own because I think it's been taken too literally. Please give me a fresh look at what an odor eliminator image could be.

Label dimensions are 11.25"x2.25"
Key wording:

Product Name: Quiet Hollow
Tag line: No one needs to know what you smoke
Also needs to include:
Directions
Remove the lid and place the container in any room where smoke is present. The contents will evaporate, neutralizing odours.

Net Wt. 14 0z. - 400 G
A spot for adding a bar code for scanners

Target Market(s)

Cigarette smokers / pot smokers / people with fire places or people who share a home with any of those categories

Requirements
Must have
• a label that fits the dimensions 11.25"x2.25" and the text / components outlined in the description
Nice to have
• A bit of humour, a sense of natural products

```html
<!DOCTYPE html>
<html lang="en">
<head>
<meta charset="utf-8">
<title>Quiet Hollow – Label</title>
<link rel="stylesheet" href="https://fonts.googleapis.com/css2?family=Arimo&family=League+Spartan:wght@400;500;700&display=swap">
<style>
  :root {
    --page: #ffffff;
    --navy: #150d45;
    --navy-mid: #1d1660;
    --smoke-blue: #3a78d0;
    --smoke-grey: #8a8fa8;
    --title-white: #ffffff;
    --title-green: #bfe2c0;
    --ink-light: #e8ecff;
    --ring: rgba(210, 214, 240, 0.75);
    --flag-red: #e0202a;
  }
  * { margin: 0; padding: 0; box-sizing: border-box; }
  html, body { width: 1200px; height: 1200px; overflow: hidden; background: var(--page); }
  .canvas { position: relative; width: 1200px; height: 1200px; }

  .label {
    position: absolute; left: 60px; top: 492px;
    width: 1080px; height: 216px; overflow: hidden;
    background: linear-gradient(90deg, var(--navy) 0%, var(--navy) 55%, var(--navy-mid) 100%);
    font-family: "League Spartan", sans-serif; color: var(--ink-light);
  }
  .smoke-photo-left {
    position: absolute; left: 0; top: 0; width: 520px; height: 216px;
    background: radial-gradient(ellipse at 30% 50%, rgba(20,14,60,0.2) 0 35%, rgba(138,143,168,0.55) 60%, rgba(21,13,69,0) 100%);
  }
  .smoke-photo-right {
    position: absolute; right: 0; top: 0; width: 600px; height: 216px;
    background: radial-gradient(ellipse at 70% 85%, rgba(58,120,208,0.85) 0%, rgba(58,120,208,0.35) 45%, rgba(21,13,69,0) 75%),
                radial-gradient(ellipse at 100% 20%, rgba(58,120,208,0.6) 0%, rgba(21,13,69,0) 45%);
  }
  .leaf-motif {
    position: absolute; left: 456px; top: 2px; width: 202px; height: 214px;
    background: radial-gradient(ellipse at 50% 55%, rgba(160,160,220,0.28) 0%, rgba(160,160,220,0) 70%);
  }
  .ring { position: absolute; left: 0; top: 0; }

  .brand-title {
    position: absolute; left: 106px; top: 32px;
    font-weight: 700; font-size: 76px; line-height: 68px; letter-spacing: -1px;
  }
  .brand-title .word-light { color: var(--title-white); display: block; }
  .brand-title .word-green { color: var(--title-green); display: block; }

  .tagline {
    position: absolute; left: 99px; top: 176px; width: 314px; height: 20px;
    border-top: 1px solid var(--ring); border-bottom: 1px solid var(--ring);
    font-weight: 500; font-size: 14.5px; line-height: 19px; color: var(--title-white);
    padding-left: 10px; white-space: nowrap;
  }

  .origin-badge {
    position: absolute; left: 682px; top: 69px; height: 27px; padding: 0 8px 0 5px;
    border: 1px solid var(--ring); border-radius: 2px;
    display: flex; align-items: center; gap: 8px;
    font-family: "Arimo", sans-serif; font-size: 16px; color: var(--ink-light);
  }
  .flag { width: 22px; height: 13px; display: block; }

  .directions { position: absolute; left: 686px; top: 110px; width: 380px; font-size: 11px; line-height: 15px; }
  .directions h2 { font-size: 11px; font-weight: 400; margin-bottom: 2px; }
  .directions p { font-weight: 400; }
  .net-weight { position: absolute; left: 685px; top: 170px; font-size: 16px; font-weight: 400; }
</style>
</head>
<body>
<main class="canvas">
  <section class="label">
    <div class="smoke-photo-left" role="img" aria-label="Photograph of drifting grey smoke"></div>
    <div class="smoke-photo-right" role="img" aria-label="Photograph of billowing blue smoke"></div>
    <div class="leaf-motif" role="img" aria-label="Line drawing of a plant leaf"></div>
    <svg class="ring" width="520" height="216" viewBox="0 0 520 216" aria-hidden="true">
      <circle cx="257" cy="108" r="184" fill="none" stroke="var(--ring)" stroke-width="1.6"/>
    </svg>

    <h1 class="brand-title">
      <span class="word-light">QUIET</span>
      <span class="word-green">HOLLOW</span>
    </h1>
    <p class="tagline">No one needs to know what you smoke</p>

    <div class="origin-badge">
      <span>Made in Canada</span>
      <svg class="flag" viewBox="0 0 22 13" aria-hidden="true">
        <rect width="22" height="13" fill="#fff"/>
        <rect width="5.5" height="13" fill="var(--flag-red)"/>
        <rect x="16.5" width="5.5" height="13" fill="var(--flag-red)"/>
        <path d="M11 3 L13 6.5 L11 9.5 L9 6.5 Z" fill="var(--flag-red)"/>
      </svg>
    </div>

    <div class="directions">
      <h2>Directions for use</h2>
      <p>Remove the lid and place the container in any room where smoke<br>is present. The contents will evaporate, neutralizing odours.</p>
    </div>
    <p class="net-weight">Net Wt. 14 0z. - 400 G</p>
  </section>
</main>
</body>
</html>
```